Business card required for IT Consultancy Business - Tealbrook Consulting.
Company provides the whole nine yards of services across IT Architecture, design and execution.
Basically we provide consulting services to help businesses make sure their technology is enabling their business strategy.
Design for front and back required.
We would like the front of the card to inlcude:
Name
Title
Mobile number
email address
www.tbkc.com.au
Company logos attached.
Thank you
Industry/Entity Type
Business
Contact Information for Business Card
Name
Title
Mobile number
email address
www.tbkc.com.au
Look and feel
Each slider illustrates characteristics of the customer's brand and the style your logo design should communicate.

```html
<!DOCTYPE html>
<html lang="en">
<head>
<meta charset="utf-8">
<title>Tealbrook Consulting – Business Card</title>
<link rel="stylesheet" href="https://fonts.googleapis.com/css2?family=Arimo:wght@400;700&display=swap">
<style>
  :root {
    --page-bg: #e9e4dc;
    --card-blue-light: #2d62ad;
    --card-blue: #17479a;
    --card-blue-deep: #0c347e;
    --frost: #e3e6ea;
    --text-light: #e8e6e1;
    --text-soft: #d6dbe4;
  }
  * { margin: 0; padding: 0; box-sizing: border-box; }
  html, body {
    width: 1200px; height: 970px; overflow: hidden;
    background: var(--page-bg);
    font-family: "Arimo", Arial, sans-serif;
  }
  .canvas {
    position: relative; width: 1200px; height: 970px;
    display: flex; align-items: center; justify-content: center;
  }
  .card {
    position: relative; width: 1000px; height: 570px; overflow: hidden;
    background:
      linear-gradient(90deg, var(--card-blue-light) 0%, var(--card-blue) 40%, var(--card-blue-deep) 62%, var(--frost) 62.1%, var(--frost) 100%);
    box-shadow: 0 10px 30px rgba(40, 30, 20, 0.25);
  }
  .card-mark-area {
    position: absolute; right: -40px; top: 20px; width: 500px; height: 530px;
  }
  .wordmark {
    position: absolute; left: 55px; top: 80px;
    color: var(--text-light); font-weight: 700; line-height: 1;
  }
  .wordmark-name { display: block; font-size: 62px; letter-spacing: 1px; }
  .wordmark-sub { display: block; font-size: 36px; letter-spacing: 5px; margin-top: 10px; padding-left: 4px; }
  .holder { position: absolute; left: 55px; top: 338px; color: var(--text-light); }
  .holder-name { font-size: 30px; font-weight: 700; letter-spacing: 0.5px; }
  .holder-title { font-size: 22px; font-weight: 400; color: var(--text-soft); margin-top: 2px; }
  .contact-list { position: absolute; left: 55px; top: 438px; list-style: none; }
  .contact-item {
    display: flex; align-items: center; gap: 14px;
    font-size: 23px; color: var(--text-soft); height: 36px;
  }
  .contact-icon { width: 22px; height: 22px; flex: none; }
</style>
</head>
<body>
<main class="canvas">
  <section class="card" aria-label="Tealbrook Consulting business card front">
    <svg class="card-mark-area" viewBox="0 0 500 530" role="img" aria-label="Large brand symbol area">
      <circle cx="250" cy="250" r="230" fill="#d7dce3"/>
    </svg>

    <div class="wordmark">
      <span class="wordmark-name">TEALBROOK</span>
      <span class="wordmark-sub">consulting</span>
    </div>

    <div class="holder">
      <p class="holder-name">DANIEL HARROW</p>
      <p class="holder-title">Managing Director</p>
    </div>

    <ul class="contact-list">
      <li class="contact-item">
        <svg class="contact-icon" viewBox="0 0 24 24" fill="none" stroke="#d6dbe4" stroke-width="2">
          <rect x="6" y="2" width="12" height="20" rx="2"/><line x1="10" y1="18" x2="14" y2="18"/>
        </svg>
        <span>(03) 5550 1427</span>
      </li>
      <li class="contact-item">
        <svg class="contact-icon" viewBox="0 0 24 24" fill="none" stroke="#d6dbe4" stroke-width="2">
          <rect x="2" y="6" width="20" height="13"/><polyline points="2,6 12,14 22,6"/>
        </svg>
        <span>hello@tbkc.com.au</span>
      </li>
      <li class="contact-item">
        <svg class="contact-icon" viewBox="0 0 24 24" fill="none" stroke="#d6dbe4" stroke-width="2">
          <circle cx="12" cy="12" r="10"/><ellipse cx="12" cy="12" rx="4" ry="10"/><line x1="2" y1="12" x2="22" y2="12"/>
        </svg>
        <span>www.tbkc.com.au</span>
      </li>
    </ul>
  </section>
</main>
</body>
</html>
```